Website Design, Ecommerce, Device Buyback, Four concepct pages

Full website design, concept and select pages.
* Home page
* Device catalog
* Order Summary

Require all design assets:
+ static images
+ color pallettes
+ fonts
Would prefer 'atomic' design elements.

Current concept site: http://vrlm.q7webnest.com/
Updates

Need extra days to review

Target Market(s)

us retail

Industry/Entity Type

Ecommerce

Number of Pages Required

3 page

Font styles to use
Serif
Sans Serif

Requirements
Must have
• * Home page
* Device catalog
* Order Summary
* Informational page

+ static images
+ color pallettes
+ fonts
Nice to have
• Would prefer 'atomic' design elements.
Additional pages nice to have:
* Form pages, eg contact form, login form
* Reviews page
* Back office pages: user management, catalog management, order management, etc.

```html
<!DOCTYPE html>
<html lang="en">
<head>
<meta charset="utf-8">
<title>DevSwap – Buy Back</title>
<link href="https://fonts.googleapis.com/css2?family=Poppins:wght@400;500;600;700&display=swap" rel="stylesheet">
<style>
:root{
  --navy:#0b1b46;
  --navy-deep:#05305b;
  --footer:#1c1e2b;
  --hero-bg:#f4f7fa;
  --blob:#e7eef8;
  --blue:#0a7cf0;
  --red:#fb2c0a;
  --green:#25b624;
  --text:#444a57;
  --muted:#6f7480;
  --card:#f2f3f8;
  --white:#ffffff;
}
*{box-sizing:border-box;margin:0;padding:0}
html,body{width:1200px;height:2586px;overflow:hidden}
body{font-family:"Poppins",sans-serif;color:var(--text);background:var(--white)}
.page{position:relative;width:1200px;height:2586px;overflow:hidden}
.abs{position:absolute}

/* header + hero */
.hero{position:absolute;left:0;top:0;width:1200px;height:702px;background:var(--hero-bg);overflow:hidden}
.hero-blob{position:absolute;left:0;top:0}
.wave{position:absolute;border-radius:50%;filter:blur(2px)}
.wave-left{left:-20px;top:140px;width:360px;height:220px;background:radial-gradient(ellipse at center,rgba(120,140,240,.28),rgba(120,170,240,0) 70%)}
.wave-right{left:900px;top:120px;width:320px;height:330px;background:radial-gradient(ellipse at center,rgba(140,130,240,.28),rgba(140,170,240,0) 70%)}
.brand{position:absolute;left:150px;top:14px;display:flex;align-items:center;gap:10px}
.brand-dot{width:56px;height:52px;border-radius:8px;background:var(--navy)}
.brand-name{font-weight:700;font-size:27px;color:var(--red);letter-spacing:-.5px}
.nav{position:absolute;top:28px;left:688px;display:flex;gap:44px;font-size:16px;color:#6b7080}
.nav a{color:inherit;text-decoration:none}
.nav .active{color:var(--navy);font-weight:500;padding-bottom:6px;border-bottom:2px solid #2fb6e6}
.nav a:nth-child(3){margin-left:-14px}
.btn-login{position:absolute;left:960px;top:24px;width:90px;height:34px;border-radius:17px;background:var(--blue);color:#fff;font-size:15px;font-weight:500;display:flex;align-items:center;justify-content:center;box-shadow:0 6px 14px rgba(10,124,240,.3)}
.hero-title{position:absolute;left:148px;top:258px;font-size:32px;line-height:41px;font-weight:700;color:var(--navy)}
.hero-copy{position:absolute;left:148px;top:353px;font-size:13.5px;line-height:23px;color:#3d4250;width:330px}
.btn-quote{position:absolute;left:148px;top:430px;width:131px;height:37px;background:var(--navy-deep);color:#fff;font-size:13.5px;font-weight:500;border-radius:2px;display:flex;align-items:center;justify-content:center}
.hero-art{position:absolute;left:558px;top:212px;width:396px;height:354px;border-radius:24px 24px 12px 12px;background:linear-gradient(160deg,#2a2d35,#090a0d)}

/* buy back */
.section-title{position:absolute;width:1200px;text-align:center;color:var(--navy)}
.bb-title{top:752px;font-size:21px;font-weight:600}
.bb-sub{top:792px;font-size:12px;color:var(--text)}
.card{position:absolute;top:898px;width:300px;height:308px;background:var(--card);border-radius:3px;text-align:center}
.card-phone{left:290px}
.card-tablet{left:621px}
.card-photo{position:absolute;top:-52px;left:50%;transform:translateX(-50%);border-radius:14px}
.photo-phone{width:110px;height:218px;background:linear-gradient(110deg,#1d1f27 0%,#3b3f4b 42%,#f2f2f4 48%,#d4d6db 100%)}
.photo-tablet{width:150px;height:214px;background:linear-gradient(130deg,#15161b 0%,#2f8fd6 35%,#53b4ea 55%,#c9cbd0 75%,#a9abb1 100%)}
.card-text{position:absolute;top:180px;left:40px;width:220px;font-size:12.5px;line-height:21px;color:var(--text)}
.btn-browse{position:absolute;top:240px;left:95px;width:110px;height:34px;border-radius:17px;background:var(--red);color:#fff;font-size:12px;font-weight:600;display:flex;align-items:center;justify-content:center}

/* how it works */
.hw-title{top:1345px;font-size:32px;font-weight:400}
.hw-title strong{font-weight:700}
.hw-sub{top:1396px;font-size:13px;line-height:24px;color:var(--muted)}
.step{position:absolute;top:1492px;width:260px;text-align:center}
.step-icon{width:76px;height:76px;border-radius:50%;margin:0 auto}
.step-1{left:91px}.step-1 .step-icon{background:var(--blue)}
.step-2{left:454px}.step-2 .step-icon{background:var(--red)}
.step-3{left:831px}.step-3 .step-icon{background:var(--green)}
.step h3{margin-top:24px;font-size:19.5px;font-weight:500;color:var(--navy)}
.step p{margin-top:10px;font-size:13px;line-height:23px;color:var(--muted)}
.step-3 p{width:260px}
.flow{position:absolute;left:0;top:1480px}

/* about */
.about{position:absolute;left:0;top:1822px;width:1200px;height:460px;background:var(--navy-deep)}
.about-art{position:absolute;left:234px;top:110px;width:272px;height:244px;border-radius:18px 18px 10px 10px;background:linear-gradient(160deg,#ffffff,#dfe7f1)}
.about-title{position:absolute;left:568px;top:110px;font-size:35px;color:#fff;font-weight:400}
.about-title strong{font-weight:700}
.about-copy{position:absolute;left:568px;top:194px;width:440px;font-size:14.5px;line-height:26.5px;color:#c4d0de}

/* footer */
.footer{position:absolute;left:0;top:2282px;width:1200px;height:304px;background:var(--footer)}
.footer-brand{position:absolute;left:0;width:1200px;top:40px;display:flex;justify-content:center;align-items:center;gap:10px}
.footer-brand .brand-dot{width:52px;height:48px;background:#fff}
.footer-brand .brand-name{color:#fff}
.footer-nav{position:absolute;top:120px;left:461px;display:flex;gap:35px;font-size:13px;color:#a5a8b3}
.socials{position:absolute;top:160px;left:515px;display:flex;gap:11px}
.socials span{width:34px;height:34px;border-radius:50%;background:#2b2e3b}
.socials span.on{background:#0a3a70}
.copyright{position:absolute;top:258px;left:160px;font-size:11px;color:#a5a8b3}
.legal{position:absolute;top:258px;left:873px;font-size:11px;color:#a5a8b3;display:flex;gap:14px}
</style>
</head>
<body>
<div class="page">

  <section class="hero">
    <svg class="hero-blob" width="1200" height="702" viewBox="0 0 1200 702" aria-hidden="true">
      <path d="M520 0 H1200 V590 C1080 620 900 600 780 520 C660 440 560 330 525 200 C505 120 500 50 520 0 Z" fill="var(--blob)"/>
    </svg>
    <div class="wave wave-left" role="img" aria-label="Soft dotted wave decoration"></div>
    <div class="wave wave-right" role="img" aria-label="Soft dotted wave decoration"></div>

    <div class="brand"><span class="brand-dot"></span><span class="brand-name">DevSwap</span></div>
    <nav class="nav"><a class="active">Home</a><a>Phones</a><a>Tablets</a></nav>
    <div class="btn-login">Login</div>

    <h1 class="hero-title">Buy Back<br>Get a Quote, Get Paid</h1>
    <p class="hero-copy">We are a leading company in the industry of computer and phone repairs throughout Florida.</p>
    <div class="btn-quote">Get a Quote</div>

    <div class="hero-art" role="img" aria-label="Illustration of a monitor holding a tablet and phone with a check mark"></div>
  </section>

  <h2 class="section-title bb-title">Buy Back</h2>
  <p class="section-title bb-sub">Bring your device into any one of our convenient locations.</p>

  <div class="card card-phone">
    <div class="card-photo photo-phone" role="img" aria-label="Photo of a black and a white smartphone"></div>
    <p class="card-text">All kinds of phones including smartphones</p>
    <div class="btn-browse">Browse</div>
  </div>
  <div class="card card-tablet">
    <div class="card-photo photo-tablet" role="img" aria-label="Photo of a tablet shown front and back"></div>
    <p class="card-text">All kinds of tablets</p>
    <div class="btn-browse">Browse</div>
  </div>

  <h2 class="section-title hw-title">How <strong>It Works</strong></h2>
  <p class="section-title hw-sub">Lorem Ipsum is simply dummy text of the printing and typesetting industry.<br>Lorem Ipsum has been the industry's standard dummy text.</p>

  <svg class="flow" width="1200" height="100" viewBox="0 0 1200 100" aria-hidden="true">
    <path d="M290 30 C350 0 380 20 410 50 C440 85 480 80 508 36" fill="none" stroke="#2946b8" stroke-width="1.6" stroke-dasharray="1.5 3.5"/>
    <polygon points="502,30 512,26 510,38" fill="#1f3fbf"/>
    <path d="M673 62 C720 85 760 75 790 40 C820 0 860 10 888 54" fill="none" stroke="#2946b8" stroke-width="1.6" stroke-dasharray="1.5 3.5"/>
    <polygon points="884,52 894,58 884,62" fill="#1f3fbf"/>
  </svg>

  <div class="step step-1">
    <div class="step-icon"></div>
    <h3>Install the app</h3>
    <p>Get an exact quote for your exact device and its condition.</p>
  </div>
  <div class="step step-2">
    <div class="step-icon"></div>
    <h3>Bring</h3>
    <p>Bring your device into any one of our convenient locations. We'll pull up your quote right away.</p>
  </div>
  <div class="step step-3">
    <div class="step-icon"></div>
    <h3>Get Paid</h3>
    <p>Get money as soon as we receive your device. We'll review the condition</p>
  </div>

  <section class="about">
    <div class="about-art" role="img" aria-label="White illustration of a monitor holding a tablet and phone with a check mark"></div>
    <h2 class="about-title">About <strong>Us</strong></h2>
    <p class="about-copy">We are a leading company in the industry of computer and phone repairs throughout Florida. Circuit Corner Mobile is the place to go for an experienced, yet affordable cell phone and computer repair store!</p>
  </section>

  <footer class="footer">
    <div class="footer-brand"><span class="brand-dot"></span><span class="brand-name">DevSwap</span></div>
    <nav class="footer-nav"><span>Home</span><span>Phones</span><span>Tablets</span><span>Contact</span></nav>
    <div class="socials"><span></span><span class="on"></span><span></span><span></span></div>
    <p class="copyright">Copyright © 2021 devswap</p>
    <p class="legal"><span>Terms of Use</span><span>|</span><span>Privacy Policy</span></p>
  </footer>

</div>
</body>
</html>
```